Zielgruppe
Halvora ist Ihr leistungsstarker und zuverlässiger Partner im Bereich Metallverarbeitung. Seit unserer Firmengründung im Jahr 2001 ist unser inhabergeführtes Unternehmen in Falkenried bei Chemnitz kontinuierlich gewachsen und beschäftigt derzeit 20 engagierte und qualifizierte Mitarbeiter.
Mit der Einweihung unserer neuen Fertigungshalle 2010 haben wir unsere Produktionsfläche auf 1.400 m2 vergrößert und können Ihnen nun einen noch umfassenderen Service anbieten.
Von der CNC-gesteuerten Teilefertigung bis zu modernsten Schweiß-, Schneid-, und Bearbeitungsanlagen – für die Realisierung Ihrer individuellen Wünsche steht uns ein innovativer Maschinenpark zur Verfügung. Wir fertigen zuverlässig und termingerecht nach Ihren Plänen oder übernehmen bei Bedarf auch die gesamte Abwicklung Ihres Projektes – alles made in germany!
Das Unternehmen spricht ausschließlich B2B Kunden an.
Die Hauptleistungsbereiche sind:
- Stahl- und Palettenbau
- Blechbearbeitung
- Edelstahlbearbeitung
- Mechanische Fertigung
Aufgabenstellung
- Mitlaufende Kontaktleiste
- Integration der Social Media Kanäle
- Sehr modernes Auftreten
- Industrielles Design
- Verlinkung zum Partnerunternehmen https://www.halvora.de/ias/index.html

```html
<!DOCTYPE html>
<html lang="de">
<head>
<meta charset="utf-8">
<title>Halvora – Metallverarbeitung</title>
<link rel="stylesheet" href="https://fonts.googleapis.com/css2?family=Outfit:wght@400;500;600;700;800&display=swap">
<style>
:root{
  --navy:#0c3a72;
  --ink:#16181d;
  --text:#5b5e66;
  --white:#ffffff;
  --grey:#c4c4c6;
  --footer:#14151a;
  --line:#0c3a72;
}
*{box-sizing:border-box;margin:0;padding:0}
html,body{width:1200px;height:2494px;overflow:hidden}
body{font-family:"Outfit",sans-serif;color:var(--ink);background:var(--white);position:relative}
.abs{position:absolute}

.service-bar{left:0;top:0;width:1200px;height:34px;background:var(--white);display:flex;align-items:center;gap:18px;padding-left:64px;font-size:12.5px;font-weight:700}
.service-bar span{display:flex;align-items:center;gap:6px}
.service-bar svg{width:10px;height:12px}

.hero{left:0;top:34px;width:1200px;height:414px;background:linear-gradient(100deg,#4a4540 0%,#6f5a4d 30%,#b2533a 42%,#8a8478 60%,#a59f92 78%,#6e6a62 100%)}
.hero-shade{left:0;top:0;width:1200px;height:414px;background:linear-gradient(90deg,rgba(20,18,16,.55) 0%,rgba(20,18,16,.25) 45%,rgba(0,0,0,0) 70%)}
.brand{left:64px;top:26px;font-size:38px;font-weight:800;letter-spacing:-.5px;color:var(--ink)}
.main-nav{left:417px;top:21px;width:587px;height:45px;background:var(--white);display:flex;align-items:center;gap:34px;padding-left:18px;font-size:14.5px;font-weight:700}
.main-nav .active{position:relative}
.main-nav .active::after{content:"";position:absolute;left:0;right:0;bottom:-14px;height:4px;background:var(--navy)}
.nav-phone{left:1004px;top:21px;width:196px;height:45px;background:var(--navy);color:var(--white);font-size:12px;font-weight:700;display:flex;align-items:center;justify-content:center;gap:6px}
.hero-title{left:64px;top:188px;font-size:31px;line-height:36px;font-weight:800;color:var(--white)}
.hero-sub{left:64px;top:280px;font-size:12.5px;line-height:15px;color:var(--white)}
.btn{display:flex;align-items:center;justify-content:center;border-radius:14px;font-size:9.5px;height:26px}
.btn-navy{background:var(--navy);color:var(--white)}
.btn-white{background:var(--white);color:var(--navy);border:1px solid var(--navy)}

.section-title{font-size:21px;line-height:26px;font-weight:800;text-transform:uppercase;color:var(--ink)}
.rule{height:3px;width:148px;background:var(--line)}
.body-copy{font-size:12px;line-height:18.3px;color:var(--text)}

.photo{overflow:hidden}
.photo-welding{background:linear-gradient(135deg,#123a78 0%,#1f4f9e 40%,#6a6e82 55%,#3e3e48 80%,#2a2a30 100%)}
.photo-sheet{background:linear-gradient(120deg,#17407e 0%,#2a5390 35%,#9aa2ad 50%,#c7ccd2 70%,#7a7f86 100%)}
.photo-grinder{background:linear-gradient(135deg,#2a3446 0%,#4b3a30 40%,#8f4630 55%,#b8a89a 75%,#4a4d55 100%)}

.products{left:0;top:916px;width:1200px;height:420px;background:linear-gradient(180deg,#1d1f25 0%,#2f333b 45%,#15171c 100%)}
.product-card{height:211px;display:flex}
.product-card .photo{width:281px;height:211px}
.product-info{width:240px;height:211px;background:var(--navy);color:var(--white);padding:38px 20px 0 22px}
.product-info h3{font-size:12px;font-weight:700;margin-bottom:22px}
.product-info p{font-size:12px;line-height:18.3px}
.more{display:inline-flex;align-items:center;gap:8px;margin-top:13px;font-size:12px}
.more u{text-underline-offset:3px}
.slider-dot{width:34px;height:34px;border-radius:50%;background:#e7e7e9;display:flex;align-items:center;justify-content:center}

.quals{left:0;top:1771px;width:600px;height:259px;background:var(--navy)}
.quals-frame{left:64px;top:41px;width:487px;height:176px;border:2px solid var(--white);padding:26px 20px 0 22px;color:var(--white)}
.quals-frame h2{font-size:21px;font-weight:800;margin-bottom:8px}
.quals-frame p{font-size:11.8px;line-height:18.3px}
.partner{left:600px;top:1771px;width:600px;height:259px;background:var(--grey)}
.partner h2{font-size:21px;font-weight:800}
.partner-name{display:flex;align-items:center;gap:8px;font-size:12px;font-weight:600;color:var(--navy)}
.partner-name i{width:14px;height:14px;background:var(--navy);display:block}

.adv{display:flex;gap:30px;width:520px}
.adv-icon{width:47px;height:47px;border-radius:50%;border:1px solid #9ab0cc;flex:none;display:flex;align-items:center;justify-content:center}
.adv h3{font-size:14.5px;font-weight:700;color:#6b6e75;margin-top:4px;margin-bottom:12px}
.adv p{font-size:11.5px;line-height:14px;color:var(--text);width:400px}

.site-footer{left:0;top:2345px;width:1200px;height:149px;background:var(--footer);color:var(--white)}
.site-footer h4{font-size:11.5px;font-weight:700}
.foot-col{font-size:10px;line-height:13px;display:flex;gap:10px}
.foot-col svg{width:9px;height:11px;margin-top:1px}
</style>
</head>
<body>

<div class="abs service-bar">
  <span><svg viewBox="0 0 10 12"><path d="M5 0C6 3 9 4 9 7.5A4 4 0 0 1 1 7.5C1 5 3 4 5 0Z" fill="#0c3a72"/></svg>Stahl- und Palettenbau</span>
  <span><svg viewBox="0 0 10 12"><path d="M5 0C6 3 9 4 9 7.5A4 4 0 0 1 1 7.5C1 5 3 4 5 0Z" fill="#0c3a72"/></svg>Blechbearbeitung</span>
  <span><svg viewBox="0 0 10 12"><path d="M5 0C6 3 9 4 9 7.5A4 4 0 0 1 1 7.5C1 5 3 4 5 0Z" fill="#0c3a72"/></svg>Edelstahlbearbeitung</span>
  <span><svg viewBox="0 0 10 12"><path d="M5 0C6 3 9 4 9 7.5A4 4 0 0 1 1 7.5C1 5 3 4 5 0Z" fill="#0c3a72"/></svg>Mechanische Fertigung</span>
</div>

<header class="abs hero" role="img" aria-label="Foto einer Industriemaschine mit rotem Werkstück in der Fertigungshalle">
  <div class="abs hero-shade"></div>
  <div class="abs brand">HALVORA</div>
  <nav class="abs main-nav">
    <span class="active">HOME</span><span>PRODUKTE</span><span>FERTIGUNG</span><span>QUALIFIKATION</span><span>KONTAKT</span>
  </nav>
  <div class="abs nav-phone">
    <svg width="12" height="12" viewBox="0 0 24 24"><path d="M6.6 10.8a15 15 0 0 0 6.6 6.6l2.2-2.2c.3-.3.7-.4 1-.2 1.1.4 2.3.6 3.6.6.6 0 1 .4 1 1V20c0 .6-.4 1-1 1A17 17 0 0 1 3 4c0-.6.4-1 1-1h3.5c.6 0 1 .4 1 1 0 1.3.2 2.5.6 3.6.1.3 0 .7-.2 1z" fill="#fff"/></svg>
    +49 (0) 3721 / 554 210 1
  </div>
  <h1 class="abs hero-title">Ihr zuverlässiger Partner im<br>Bereich Metallverarbeitung</h1>
  <p class="abs hero-sub">Bei Fragen zu unserem Leistungsangebot sind wir nur<br>einen Anruf oder eine E-Mail entfernt.</p>
  <div class="abs btn btn-navy" style="left:64px;top:329px;width:87px">KONTAKT</div>
  <div class="abs btn btn-white" style="left:171px;top:329px;width:152px">+49 (0)3721 / 554 210 1</div>
</header>

<section>
  <h2 class="abs section-title" style="left:64px;top:521px">Herzlich Willkommen bei Halvora<br>in Falkenried</h2>
  <div class="abs rule" style="left:64px;top:581px"></div>
  <div class="abs body-copy" style="left:65px;top:611px;width:455px">
    <p>Halvora ist Ihr leistungsstarker und zuverlässiger Partner im Bereich Metallverarbeitung. Seit unserer Firmengründung im Jahr 2001 ist unser inhabergeführtes Unternehmen in Falkenried bei Chemnitz kontinuierlich gewachsen und beschäftigt derzeit 20 engagierte und qualifizierte Mitarbeiter.</p>
    <p style="margin-top:18px">Mit der Einweihung unserer neuen Fertigungshalle 2010 haben wir unsere Produktionsfläche auf 1.400 m2 vergrößert und können Ihnen nun einen noch umfassenderen Service anbieten.</p>
  </div>
  <div class="abs photo photo-welding" style="left:649px;top:513px;width:488px;height:366px" role="img" aria-label="Foto eines Schweißers mit Schutzhelm bei der Arbeit, blau eingefärbt"></div>
</section>

<section class="abs products" role="img" aria-label="Dunkles Hintergrundfoto mit gestapelten Stahlrohren">
  <h2 class="abs" style="left:0;width:1162px;top:48px;text-align:center;font-size:21px;font-weight:800;color:#fff">UNSERE PRODUKTE</h2>
  <div class="abs" style="left:493px;top:86px;width:177px;height:3px;background:#fff"></div>
  <div class="abs product-card" style="left:64px;top:155px">
    <div class="photo photo-grinder" role="img" aria-label="Foto: Arbeiter schleift ein Stahlprofil, Funkenflug"></div>
    <div class="product-info"><h3>LADUNGSTRÄGER</h3><p>Gut aliquip ex ea commodo<br>consequat. Duis aute irure dolor<br>in reprehenderit in voluptate</p>
      <span class="more"><u>Mehr erfahren</u><svg width="18" height="8" viewBox="0 0 18 8"><path d="M0 4h16M13 1l3 3-3 3" stroke="#fff" fill="none"/></svg></span></div>
  </div>
  <div class="abs product-card" style="left:616px;top:155px">
    <div class="photo photo-grinder" role="img" aria-label="Foto: Arbeiter schleift ein Stahlprofil, Funkenflug"></div>
    <div class="product-info"><h3>SPEZIALKONSTRUKTIONEN</h3><p>Gut aliquip ex ea commodo<br>consequat. Duis aute irure dolor<br>in reprehenderit in voluptate</p>
      <span class="more"><u>Mehr erfahren</u><svg width="18" height="8" viewBox="0 0 18 8"><path d="M0 4h16M13 1l3 3-3 3" stroke="#fff" fill="none"/></svg></span></div>
  </div>
  <div class="abs slider-dot" style="left:43px;top:247px"><svg width="8" height="14" viewBox="0 0 8 14"><path d="M7 1L1 7l6 6" stroke="#999" fill="none"/></svg></div>
  <div class="abs slider-dot" style="left:1124px;top:247px"><svg width="8" height="14" viewBox="0 0 8 14"><path d="M1 1l6 6-6 6" stroke="#999" fill="none"/></svg></div>
</section>

<section>
  <div class="abs photo photo-sheet" style="left:77px;top:1374px;width:489px;height:366px" role="img" aria-label="Foto eines gebogenen Edelstahlblechs, teilweise blau eingefärbt"></div>
  <h2 class="abs section-title" style="left:648px;top:1416px;line-height:28px">Das Unternehmen<br>für Metallverarbeitung</h2>
  <div class="abs rule" style="left:649px;top:1475px"></div>
  <p class="abs body-copy" style="left:649px;top:1498px;width:462px">Lorem ipsum dolor sit amet, consectetur adipisicing elit, sed do eiusmod tempor incididunt ut labore et dolore magna aliqua. Ut enim ad minim veniam, quis nostrud exercitation ullamco laboris nisi ut aliquip ex ea commodo consequat. Duis aute irure dolor in reprehenderit in voluptate velit esse cillum dolore eu fugiat nulla pariatur. Excepteur sint occaecat cupidatat non proident, sunt in culpa qui officia deserunt mollit anim id est laborum. Sed ut perspiciatis unde omnis iste natus error sit voluptatem accusantium doloremque laudantium, totam rem aperiam, eaque ipsa quae ab illo inventore veritatis et quasi architecto beatae vitae dicta sunt explicabo.</p>
  <div class="abs btn btn-navy" style="left:649px;top:1665px;width:138px">UNSERE PRODUKTE</div>
</section>

<section class="abs quals">
  <div class="abs quals-frame">
    <h2>UNSERE QUALIFIKATIONEN</h2>
    <p>Lorem ipsum dolor sit amet, consectetur adipiscing elit, sed do eiusmod tempor incididunt ut labore et dolore magna aliqua. Quis ipsum suspendisse ultrices gravida. Risus commodo viverra maecenas accumsan lacus vel facilisis.</p>
    <span class="more" style="margin-top:16px"><u>Zu den Qualifikationen</u><svg width="18" height="8" viewBox="0 0 18 8"><path d="M0 4h16M13 1l3 3-3 3" stroke="#fff" fill="none"/></svg></span>
  </div>
</section>
<section class="abs partner">
  <h2 class="abs" style="left:48px;top:67px">UNSER PARTNERUNTERNEHMEN</h2>
  <p class="abs body-copy" style="left:49px;top:108px;width:450px;color:#333">Norvant Anlagenservice ist Ihr leistungsstarker und zuverlässiger Partner für Aufzugmontage, Fahr-treppenmontage, Fahrsteigmontage und die Montage von Fassadenliften und Befahranlagen sowie deren Wartung.</p>
  <div class="abs partner-name" style="left:49px;top:190px"><i></i>Norvant Anlagenservice</div>
</section>

<section>
  <h2 class="abs section-title" style="left:63px;top:2066px">Ihre Vorteile im Überblick</h2>
  <div class="abs rule" style="left:64px;top:2100px"></div>
  <div class="abs adv" style="left:64px;top:2143px">
    <div class="adv-icon"><svg width="18" height="20" viewBox="0 0 18 20" fill="none" stroke="#0c3a72"><circle cx="9" cy="8" r="4.5"/><path d="M7 14h4M7.5 16.5h3M9 0v1.5M1 8h1.5M15.5 8H17M3.5 2.5l1 1M14.5 2.5l-1 1"/></svg></div>
    <div><h3>HERSTELLER-QUALIFIKATIONEN</h3><p>Lorem ipsum dolor sit amet, consetetur sadipscing elitr, sed diam nonumy eirmod tempor invidunt ut labore et dolore magna alidiam voluptua</p></div>
  </div>
  <div class="abs adv" style="left:649px;top:2143px">
    <div class="adv-icon"><svg width="18" height="18" viewBox="0 0 18 18" fill="none" stroke="#0c3a72"><path d="M1 8h3v9H1zM4 16h9l3-7H10l1-6-3 0-4 5"/></svg></div>
    <div><h3>Interne Qualitätssicherung</h3><p>Lorem ipsum dolor sit amet, consetetur sadipscing elitr, sed diam nonumy eirmod tempor invidunt ut labore et dolore magna alidiam voluptua</p></div>
  </div>
  <div class="abs adv" style="left:64px;top:2218px">
    <div class="adv-icon"><svg width="20" height="18" viewBox="0 0 20 18" fill="none" stroke="#0c3a72"><rect x="1" y="3" width="15" height="13"/><path d="M1 7h15M5 1v4M12 1v4"/><circle cx="16" cy="14" r="3"/></svg></div>
    <div><h3>Realisierung individueller Wünsche</h3><p>Lorem ipsum dolor sit amet, consetetur sadipscing elitr, sed diam nonumy eirmod tempor invidunt ut labore et dolore magna alidiam voluptua</p></div>
  </div>
  <div class="abs adv" style="left:649px;top:2218px">
    <div class="adv-icon"><svg width="18" height="18" viewBox="0 0 18 18" fill="none" stroke="#0c3a72"><path d="M9 1l2.4 5 5.4.6-4 3.7 1.1 5.4L9 13l-4.9 2.7 1.1-5.4-4-3.7L6.6 6z"/></svg></div>
    <div><h3>Hochmoderne Fertigungshalle</h3><p>Lorem ipsum dolor sit amet, consetetur sadipscing elitr, sed diam nonumy eirmod tempor invidunt ut labore et dolore magna alidiam voluptua</p></div>
  </div>
</section>

<footer class="abs site-footer">
  <h4 class="abs" style="left:64px;top:27px">Kontakt</h4>
  <div class="abs" style="right:63px;top:27px;font-size:12px;font-weight:600">© 2023 HALVORA | Alle Rechte vorbehalten | Impressum</div>
  <div class="abs foot-col" style="left:64px;top:59px">
    <svg viewBox="0 0 9 11"><path d="M4.5 0A3.5 3.5 0 0 0 1 3.5C1 6 4.5 11 4.5 11S8 6 8 3.5A3.5 3.5 0 0 0 4.5 0z" fill="#0c3a72"/></svg>
    <div>HALVORA<br>Inhaber: Jonas Kretzer<br>Birkenweg 7<br>09418 Falkenried</div>
  </div>
  <div class="abs foot-col" style="left:248px;top:59px">
    <svg viewBox="0 0 9 11"><path d="M2 1l2 2-1 1.5c.6 1.3 1.4 2.1 2.5 2.6L7 6l2 2-1.5 2C4 10 .5 6 0 2.5z" fill="#0c3a72"/></svg>
    <div>Telefon: 03721 / 554 210 1<br>Telefax: 03721 / 554 210 3<br>E-Mail: info@halvora.de<br>www.halvora.de</div>
  </div>
</footer>

</body>
</html>
```